E-Waste Recycling Company Business Card

New Electronic Recycling Company based in Long Island, New York called "Baron Rustwell" We take outdated computers, components, electrical wire, circuit breakers, ink cartridges, etc. We look mostly for donated items that we recycle for our customers but will pay for large quantities from businesses. The design should reflect that we are environmentally friendly and our unique Quadra Purge process that ensures all personal data is wiped clean off hard drives. Please use our attached logo
Electrical

```html
<!DOCTYPE html>
<html lang="en">
<head>
<meta charset="utf-8">
<title>Baron Rustwell – Business Card</title>
<link rel="stylesheet" href="https://fonts.googleapis.com/css2?family=Open+Sans:wght@400;600;700&display=swap">
<style>
  :root {
    --stage: #6a6a6c;
    --card: #ffffff;
    --green: #3fae49;
    --ink: #222222;
  }
  * { margin: 0; padding: 0; box-sizing: border-box; }
  html, body {
    width: 1200px;
    height: 572px;
    overflow: hidden;
  }
  body {
    position: relative;
    background: var(--stage);
    font-family: "Open Sans", Arial, sans-serif;
    color: var(--ink);
  }
  .card {
    position: absolute;
    top: 158px;
    width: 425px;
    height: 243px;
    background: var(--card);
  }
  .card--front { left: 149px; }
  .card--back  { left: 634px; }

  .contact {
    position: absolute;
    left: 47px;
    top: 62px;
  }
  .contact__name {
    font-size: 16px;
    font-weight: 600;
    color: var(--green);
    line-height: 20px;
  }
  .contact__title {
    font-size: 9.5px;
    line-height: 12px;
  }
  .contact__address {
    margin-top: 13px;
    font-size: 9.5px;
    line-height: 13px;
  }
  .contact__list {
    list-style: none;
    margin-top: 11px;
    font-size: 9px;
  }
  .contact__item {
    display: flex;
    align-items: center;
    gap: 6px;
    height: 14.5px;
  }
  .contact__icon {
    width: 9px;
    height: 9px;
    fill: none;
    stroke: var(--green);
    stroke-width: 1.4;
  }
  .contact__icon--solid { fill: var(--green); stroke: none; }

  .wordmark {
    position: absolute;
    top: 124px;
    transform: translate(-50%, -50%);
    display: flex;
    flex-direction: column;
    align-items: center;
    gap: 10px;
    font-size: 23px;
    font-weight: 700;
    line-height: 26px;
    text-align: center;
    color: var(--green);
  }
  .card--front .wordmark { left: 304px; }
  .card--back .wordmark  { left: 206px; }
  .wordmark__dot {
    width: 92px;
    height: 92px;
    border-radius: 50%;
    background: var(--green);
  }
</style>
</head>
<body>

<section class="card card--front">
  <div class="contact">
    <p class="contact__name">Milo Garrick</p>
    <p class="contact__title">Managing Director</p>
    <p class="contact__address">Co. Street, Building<br>City/State,Zip Code</p>
    <ul class="contact__list">
      <li class="contact__item">
        <svg class="contact__icon contact__icon--solid" viewBox="0 0 10 10" aria-hidden="true"><path d="M2 0.5 L3.6 2.6 L2.8 3.6 Q4 6 6.4 7.2 L7.4 6.4 L9.5 8 L8.4 9.5 Q2.5 9 0.5 1.6 Z"/></svg>
        <span>000-000-0000</span>
      </li>
      <li class="contact__item">
        <svg class="contact__icon" viewBox="0 0 10 10" aria-hidden="true"><rect x="0.7" y="1.8" width="8.6" height="6.4"/><path d="M0.7 1.8 L5 5.4 L9.3 1.8"/></svg>
        <span>info@youremail.com</span>
      </li>
      <li class="contact__item">
        <svg class="contact__icon" viewBox="0 0 10 10" aria-hidden="true"><circle cx="5" cy="5" r="4.3"/><ellipse cx="5" cy="5" rx="1.9" ry="4.3"/><path d="M0.7 5 H9.3"/></svg>
        <span>www.yourwebsite.com</span>
      </li>
    </ul>
  </div>
  <div class="wordmark">
    <span class="wordmark__dot"></span>
    <span class="wordmark__name">Baron<br>Rustwell</span>
  </div>
</section>

<section class="card card--back">
  <div class="wordmark">
    <span class="wordmark__dot"></span>
    <span class="wordmark__name">Baron<br>Rustwell</span>
  </div>
</section>

</body>
</html>
```